Crestfield Automotive Business Card

Automotive repair , all makes including Asian and European Imports. QMR Certified (Logo),Chatterbook (logo), Pingly+ (logo)

Industry/Entity Type

Automotive

Contact Information for Business Card

Crestfield Automotive, Ray Hobart Owner, 3817 Larch Ave. Dunvale, Nd 58402. Website crestfieldautomotive.example. (555) 641-0938

```html
<!DOCTYPE html>
<html lang="en">
<head>
<meta charset="utf-8">
<title>Crestfield Automotive Business Card</title>
<link href="https://fonts.googleapis.com/css2?family=Open+Sans:wght@400;600;700;800&display=swap" rel="stylesheet">
<style>
  :root {
    --brand-blue: #1f3f9a;
    --brand-red: #d0232c;
    --ink: #1d1d1d;
    --card-white: #ffffff;
    --photo-grey-light: #a9a9a9;
    --photo-grey-dark: #7c7c7c;
    --stage: #ececec;
  }
  * { box-sizing: border-box; margin: 0; padding: 0; }
  html, body { width: 1200px; height: 1000px; overflow: hidden; }
  body {
    position: relative;
    background: var(--stage);
    font-family: "Open Sans", Arial, sans-serif;
    color: var(--ink);
  }
  .card { position: absolute; overflow: hidden; box-shadow: 0 3px 10px rgba(0,0,0,.25); }

  /* Front */
  .card-front { left: 299px; top: 105px; width: 604px; height: 360px; background: var(--card-white); }
  .brand-mark {
    position: absolute; right: 70px; top: 38px; text-align: right;
    color: var(--brand-blue); font-weight: 800; line-height: 1;
  }
  .brand-mark .brand-line-1 { display: block; font-size: 50px; letter-spacing: -1px; }
  .brand-mark .brand-line-2 { display: block; font-size: 30px; letter-spacing: 2px; margin-top: 6px; text-transform: uppercase; }

  .person { position: absolute; left: 30px; top: 194px; }
  .person-name { font-size: 19px; font-weight: 700; color: var(--brand-blue); line-height: 1.1; }
  .person-role { font-size: 14px; color: var(--brand-red); line-height: 1.2; }

  .credentials {
    position: absolute; right: 30px; top: 212px;
    display: flex; align-items: center; gap: 8px;
    font-size: 14px; font-weight: 600; color: var(--brand-red);
  }
  .social { display: flex; align-items: center; gap: 4px; font-size: 10px; font-weight: 600; color: var(--brand-blue); }
  .social-dot { width: 10px; height: 10px; border-radius: 50%; background: var(--brand-blue); }
  .social-pingly .social-dot { background: var(--brand-red); }
  .social-pingly { color: var(--brand-red); }

  .divider { position: absolute; left: 30px; right: 29px; top: 240px; height: 1.5px; background: var(--brand-blue); }
  .divider-accent { position: absolute; left: 30px; width: 98px; top: 238px; height: 3px; background: var(--brand-blue); }

  .contact { position: absolute; left: 30px; top: 266px; font-size: 15px; line-height: 21px; }
  .contact-row { display: flex; align-items: center; gap: 5px; }
  .contact-row svg { width: 11px; height: 11px; }

  .address { position: absolute; right: 29px; top: 266px; font-size: 15px; line-height: 21px; text-align: right; }

  .card-bands { position: absolute; left: 0; bottom: 0; width: 604px; height: 29px; }

  /* Backs */
  .card-back { top: 544px; width: 562px; height: 336px; }
  .card-back-plain { left: 24px; }
  .card-back-tagline { left: 616px; }
  .engine-photo {
    position: absolute; inset: 0;
    background: radial-gradient(ellipse at 50% 45%, var(--photo-grey-dark) 0%, var(--photo-grey-light) 75%);
  }
  .back-mark {
    position: absolute; left: 0; right: 0; top: 82px; text-align: center;
    color: var(--brand-blue); font-weight: 800; line-height: 1;
  }
  .back-mark .brand-line-1 { display: block; font-size: 74px; letter-spacing: -1px; }
  .back-mark .brand-line-2 { display: block; font-size: 42px; letter-spacing: 3px; margin-top: 10px; text-transform: uppercase; }
  .tagline {
    position: absolute; left: 0; right: 0; top: 294px; text-align: center;
    font-size: 13px; font-weight: 600; color: #ffffff; text-transform: uppercase;
  }
</style>
</head>
<body>

<section class="card card-front">
  <div class="brand-mark">
    <span class="brand-line-1">Crestfield</span>
    <span class="brand-line-2">Automotive</span>
  </div>

  <div class="person">
    <div class="person-name">Ray Hobart</div>
    <div class="person-role">Owner</div>
  </div>

  <div class="credentials">
    <span class="cert">QMR Certified</span>
    <span class="social social-chatter"><span class="social-dot"></span>Chatterbook</span>
    <span class="social social-pingly"><span class="social-dot"></span>Pingly+</span>
  </div>

  <div class="divider"></div>
  <div class="divider-accent"></div>

  <div class="contact">
    <div class="contact-row">
      <svg viewBox="0 0 12 12" aria-hidden="true"><path d="M3 1 C1 2 1 5 4 8 C7 11 10 11 11 9 L9 7 L7.5 8 C6 7 5 6 4 4.5 L5 3 Z" fill="var(--brand-red)"/></svg>
      <span>(555) 641-0938</span>
    </div>
    <div class="contact-row">
      <svg viewBox="0 0 12 12" aria-hidden="true"><g fill="none" stroke="var(--brand-red)" stroke-width="1.2"><circle cx="6" cy="6" r="5"/><ellipse cx="6" cy="6" rx="2.2" ry="5"/><line x1="1" y1="6" x2="11" y2="6"/></g></svg>
      <span>crestfieldautomotive.example</span>
    </div>
  </div>

  <div class="address">
    <div>3817 Larch Ave. Dunvale</div>
    <div>Nd 58402</div>
  </div>

  <svg class="card-bands" viewBox="0 0 604 29" aria-hidden="true">
    <polygon points="0,0 308,0 291,29 0,29" fill="var(--brand-blue)"/>
    <polygon points="313,0 604,0 604,29 296,29" fill="var(--brand-red)"/>
  </svg>
</section>

<section class="card card-back card-back-plain">
  <div class="engine-photo" role="img" aria-label="Faded grey photo of a car engine bay"></div>
  <div class="back-mark">
    <span class="brand-line-1">Crestfield</span>
    <span class="brand-line-2">Automotive</span>
  </div>
</section>

<section class="card card-back card-back-tagline">
  <div class="engine-photo" role="img" aria-label="Faded grey photo of a car engine bay"></div>
  <div class="back-mark">
    <span class="brand-line-1">Crestfield</span>
    <span class="brand-line-2">Automotive</span>
  </div>
  <div class="tagline">All makes including Asian and European imports</div>
</section>

</body>
</html>
```